my website is toncielbrode.com. (brand name is ton ciel brodé) This is just a template that i have choose for. The content and the pictures are not about my business just the template.
I would like to have 4 pages for now. 1 homepage, which will be an overview for all pages, it is right now in this way. It will directly highlight my story. My website will tell an exclusive story about details which makes the difference and will make people happy with very small things. It will be art related but very stylish as well. I also want to have a event agenda on my homepage where people can see where my next event is. Page 2 my blog, where I will write weekly about mindset, lifestyle and details. Inspiration place for people who are looking for unique and exclusive approaches in life. Page 3 shop, where I will sell my stuff which is handmade and unique, it will be limited edition stuff. Mostly I will make the designs from marbling art, which I am a teacher for. (https://www.vidorama-example.com/watch?v=Xk3pQr7LmZa) check this video out for more. Page 4 is book page. Here people will be able to book private or group classes for marbling art (check the video). I have already a community of more than 500 people on join nest, which will be my public as well. I wanna implement the join nest button on this page as well. to be able to track.

This is about my website. I also need a logo for my brand, which will suit my website and my goals.

I can also give you a reference website, which really like as structure and style;
https://www.brightmorrowgoods-example.com/products/the-quiet-ledger?gclid=Zx8RtYpWq2LmN4vBcD6sKjH3gFaE9uIoP1lKzXcVbNm7QwErTyUiOp0AsDfGhJkLzXcVbNm5Qw2ErTyUi_oPaSd8FgHjKlZxC_vbNQ

ton ciel brodé

4 page

• I can also give you a reference website, which really like as structure and style;
• https://www.brightmorrowgoods-example.com/products/the-quiet-ledger?gclid=Zx8RtYpWq2LmN4vBcD6sKjH3gFaE9uIoP1lKzXcVbNm7QwErTyUiOp0AsDfGhJkLzXcVbNm5Qw2ErTyUi_oPaSd8FgHjKlZxC_vbNQ

```html
<!DOCTYPE html>
<html lang="en">
<head>
<meta charset="utf-8">
<title>ton ciel brodé</title>
<link href="https://fonts.googleapis.com/css2?family=Roboto:wght@300;400;500;700&family=Open+Sans:wght@400&display=swap" rel="stylesheet">
<style>
:root{
  --ink:#222;
  --muted:#555;
  --dark:#2c2c2e;
  --band:#333335;
  --paper:#fff;
  --soft:#f1f1f1;
  --card:#efe9e5;
  --accent:#7e1a1a;
  --price:#c4161c;
  --contact:#4b4741;
  --field:#5d5952;
  --footer:#2a2a2a;
}
*{box-sizing:border-box;margin:0;padding:0}
html,body{width:1200px;height:3309px;overflow:hidden}
body{font-family:"Roboto",Arial,sans-serif;color:var(--ink);background:var(--paper);position:relative}
.abs{position:absolute}
p{line-height:1.55}

/* header */
.topbar{top:0;left:0;width:1200px;height:48px;border-bottom:1px solid #ddd;background:var(--soft)}
.topbar .links{left:161px;top:14px;display:flex;gap:38px;font-size:12px;letter-spacing:.3px;color:#333}
.cart{left:920px;top:8px;display:flex;gap:10px;align-items:center}
.cart strong{display:block;font-size:12px;color:var(--accent)}
.cart span{font-size:11px;color:#666}
.masthead{top:48px;left:0;width:1200px;height:89px;background:var(--soft)}
.brand{left:161px;top:26px;display:flex;align-items:center;gap:12px}
.brand-dot{width:34px;height:34px;background:var(--dark)}
.brand-name{font-size:27px;font-weight:500;color:var(--dark)}
.nav{left:717px;top:32px;display:flex;gap:60px;font-size:14px;font-weight:500;color:#222}

/* hero */
.hero{top:137px;left:0;width:1200px;height:492px;background:linear-gradient(135deg,#3b3530 0%,#6e4a3e 40%,#8b5d4d 60%,#4a4a4a 100%)}
.hero-circle{left:645px;top:173px;width:396px;height:396px;border-radius:50%;background:rgba(40,60,120,.72);border:6px solid rgba(255,255,255,.25);color:#fff;text-align:center;padding-top:70px}
.hero-circle .kicker{font-size:30px;font-weight:300;letter-spacing:1px}
.hero-circle h1{font-size:36px;font-weight:500;letter-spacing:1px;line-height:1.1}
.hero-circle p{font-size:12.5px;margin:18px 48px 0;line-height:1.55}
.btn-light{display:inline-flex;align-items:center;gap:10px;margin-top:28px;background:#fff;color:#222;font-size:12px;font-weight:700;padding:9px 12px 9px 20px;border-radius:2px}
.btn-light i{width:26px;height:26px;border-radius:50%;background:var(--dark);display:inline-block}

/* welcome */
.welcome{top:629px;left:0;width:1200px;height:161px;background:var(--band);color:#fff;overflow:hidden}
.welcome .title{left:161px;top:40px;line-height:1}
.welcome .title small{display:block;font-size:30px;font-weight:300}
.welcome .title strong{display:block;font-size:34px;font-weight:500;margin-top:6px}
.welcome .divider{left:430px;top:20px;width:1px;height:121px;background:#555}
.welcome .copy{left:465px;top:16px;width:640px;font-size:11.5px;color:#ddd}
.welcome .copy p{line-height:1.4}
.welcome .copy p+p{margin-top:8px}

/* book */
.book-img{left:161px;top:838px;width:320px;height:331px;background:linear-gradient(140deg,#5a3c6e,#c9a58f 45%,#7b5b7f 70%,#3f2f4a)}
.book{left:514px;top:846px;width:490px}
.book h2{font-size:21px;font-weight:700;margin-bottom:12px;color:#222}
.book p{font-size:12.5px;color:#333}
.book p+p{margin-top:14px}
.btn-dark{display:inline-flex;align-items:center;gap:8px;background:var(--dark);color:#fff;font-size:11px;font-weight:700;padding:12px 14px;margin-top:24px}
.btn-dark i{width:10px;height:10px;border-radius:50%;background:#fff;display:inline-block}

/* video */
.video{top:1209px;left:0;width:593px;height:452px;background:linear-gradient(160deg,#6a3a3a,#2d4d8a 50%,#1b2f6a 70%,#4b4040)}
.video-label{left:0;top:1370px;width:593px;text-align:center;color:#fff}
.video-label strong{display:block;font-size:40px;font-weight:700;margin-top:8px;line-height:1.1}
.video-label span{display:block;font-size:13px;font-weight:700}
.howto{top:1209px;left:593px;width:607px;height:452px;background:#e9e9e9}
.howto .head{left:0;top:85px;width:607px;text-align:center}
.howto .head small{display:block;font-size:22px;font-weight:300;color:#555}
.howto .head h2{font-size:28px;font-weight:500;color:#222}
.howto .intro{left:70px;top:170px;width:470px;font-size:11.5px;text-align:center;color:#333}
.features{left:0;top:265px;width:607px;height:187px;display:flex;border-top:1px solid #d0d0d0}
.feature{flex:1;text-align:center;border-right:1px solid #d0d0d0;padding-top:32px}
.feature:last-child{border-right:0}
.feature h3{font-size:15px;font-weight:700;margin:10px 0 4px}
.feature p{font-size:10.5px;color:#444;margin:0 22px;line-height:1.45}

/* products */
.section-title{left:0;width:1200px;display:flex;justify-content:center;align-items:center;gap:18px}
.section-title b{display:block;height:2px;background:#333}
.section-title h2{font-weight:400;color:#222}
.products-title{top:1700px}
.products-title h2{font-size:31px}
.products-title b{width:170px}
.product{top:1758px;width:210px;text-align:center}
.product .thumb{height:294px;background:var(--card);border:1px solid #ddd}
.product h3{font-size:16px;font-weight:500;margin-top:14px}
.product .sku{font-size:10px;color:#777;margin-top:4px}
.product .price{font-size:16px;color:var(--price);font-weight:500;margin-top:4px}
.arrow{top:1887px;width:30px;height:30px;background:#111}

/* blog */
.blog-bg{top:2190px;left:0;width:1200px;height:457px;background:#f4f4f4}
.blog-title{top:2200px}
.blog-title h2{font-size:22px;font-weight:500}
.blog-title b{width:170px}
.post{top:2279px;width:278px}
.post .thumb{height:176px}
.post .date{font-size:11.5px;margin-top:16px;color:#222}
.post h3{font-size:14px;font-weight:500;color:var(--accent);margin-top:14px;text-transform:uppercase}
.post p{font-size:11px;color:#333;margin-top:10px;line-height:1.5}

/* contact */
.contact{top:2647px;left:0;width:593px;height:468px;background:var(--contact);color:#fff}
.contact h2{left:161px;top:38px;font-size:27px;font-weight:500}
.contact .tag{left:161px;top:75px;font-size:10.5px}
.field-label{font-size:11px;display:flex;align-items:center;gap:6px}
.field{height:32px;background:var(--field);margin-top:6px;width:200px}
.contact .btn-dark{background:#1e1e1e;margin:0}
.contact-img{top:2647px;left:593px;width:607px;height:468px;background:linear-gradient(150deg,#3d2f25,#7ec2b4 45%,#e39aa1 60%,#6f9e78 80%,#3d3a30)}

/* newsletter */
.newsletter{top:3115px;left:0;width:1200px;height:101px;background:#fff}
.newsletter h2{left:181px;top:30px;font-family:"Open Sans",Arial,sans-serif;font-weight:400;font-size:31px;color:#222}
.newsletter .input{left:358px;top:38px;width:545px;height:34px;border:1px solid #ccc;font-size:11px;color:#666;padding:10px}
.newsletter .btn-dark{left:910px;top:38px;margin:0;height:34px;padding:10px 16px;position:absolute}

/* footer */
.footer{top:3216px;left:0;width:1200px;height:93px;background:var(--footer);color:#ccc;text-align:center}
.social{display:flex;justify-content:center;gap:10px;margin-top:26px}
.social i{width:16px;height:16px;border-radius:50%;border:1px solid #aaa;display:block}
.footer p{font-size:11px;margin-top:10px}
</style>
</head>
<body>

<header>
  <div class="abs topbar">
    <nav class="abs links"><span>MY ACCOUNT</span><span>MY WISHLIST</span><span>CHECKOUT</span><span>LOG IN</span></nav>
    <div class="abs cart">
      <svg width="24" height="20" viewBox="0 0 24 20"><path d="M2 6h20l-3 11H5z" fill="none" stroke="#333" stroke-width="2"/><path d="M8 6l4-5 4 5" fill="none" stroke="#333" stroke-width="2"/></svg>
      <div><strong>Shopping Cart:</strong><span>(0) Cart Subtotal: $0.00</span></div>
    </div>
  </div>
  <div class="abs masthead">
    <div class="abs brand"><span class="brand-dot"></span><span class="brand-name">ton ciel brodé</span></div>
    <nav class="abs nav"><span>HOME</span><span>MY BLOG</span><span>SHOP ⌄</span><span>BOOK</span></nav>
  </div>
</header>

<section class="abs hero" role="img" aria-label="Marbling tray with swirled paint and jars of colour on a workbench"></section>
<div class="abs hero-circle">
  <div class="kicker">OUR NEW</div>
  <h1>ARRIVALS ARE HERE</h1>
  <p>ton ciel brodé is a leading Online Store. We provide an unparalleled selection of the very best quality products, an easy and comfortable shopping experience, expedited shipping offers, and exceptional customer service. Check out our collection of new arrivals, best-sellers, and clearance items today.</p>
  <span class="btn-light">SHOP NOW <i></i></span>
</div>

<section class="abs welcome">
  <div class="abs title"><small>WELCOME</small><strong>TON CIEL BRODÉ</strong></div>
  <div class="abs divider"></div>
  <div class="abs copy">
    <p>Lorem Ipsum is simply dummy text of the printing and typesetting industry. Lorem Ipsum has been the industry's standard dummy text ever since the 1500s, when an unknown printer took a galley of type and scrambled it to make a type specimen book. It has survived not only five centuries, but also the leap into electronic typesetting, remaining essentially unchanged. It was popularised in the 1960s with the release of Letraset sheets...</p>
    <p>Lorem Ipsum is simply dummy text of the printing and typesetting industry. Lorem Ipsum has been the industry's standard dummy text ever since the 1500s, when an unknown printer took a galley of type and scrambled it to make a type specimen book. It has survived not only five centuries...</p>
  </div>
</section>

<div class="abs book-img" role="img" aria-label="Close-up of marbled paper with purple and cream cells"></div>
<section class="abs book">
  <h2>BOOK PRIVATE OR GROUP</h2>
  <p>Lorem Ipsum is simply dummy text of the printing and typesetting industry. Lorem Ipsum has been the industry's standard dummy text ever since the 1500s, when an unknown printer took a galley of type and scrambled it to make a type specimen book. It has survived not only five centuries, but also the leap into electronic typesetting, remaining essentially unchanged. It was popularised in the 1960s with the release of Letraset sheets containing Lorem Ipsum passages, and more recently with desktop publishing software like Aldus...</p>
  <p>Lorem Ipsum is simply dummy text of the printing and typesetting industry. Lorem Ipsum has been the industry's standard dummy text ever since the 1500s, when an unknown printer took a galley of type and scrambled it to make a type specimen book. It has survived not only five centuries...</p>
  <span class="btn-dark"><i></i>CHECK THE VIDEO</span>
</section>

<section class="abs video" role="img" aria-label="Hands working over a blue marbling tray during a class"></section>
<div class="abs video-label">
  <svg width="60" height="60" viewBox="0 0 60 60"><circle cx="30" cy="30" r="27" fill="none" stroke="#fff" stroke-width="3" opacity=".8"/><path d="M24 18l18 12-18 12z" fill="#fff" opacity=".85"/></svg>
  <strong>VIDEO</strong><span>TON CIEL BRODÉ</span>
</div>

<section class="abs howto">
  <div class="abs head"><small>HOW TO PAINT ON WATER FOR</small><h2>PAPER MARBLING AND EBRU ART.</h2></div>
  <p class="abs intro">Lorem Ipsum is simply dummy text of the printing and typesetting industry. Lorem Ipsum has been the industry's standard dummy text ever since the 1500s, when an unknown printer took a galley of type and scrambled it to make a type specimen book. It has survived not only five centuries, but also the leap into electronic typesetting, remaining essentially unchanged.</p>
  <div class="abs features">
    <div class="feature">
      <svg width="34" height="30" viewBox="0 0 34 30"><path d="M3 2v25h29" fill="none" stroke="#2f4a7a" stroke-width="2"/><path d="M7 22l7-8 6 5 10-12" fill="none" stroke="#2f4a7a" stroke-width="2"/></svg>
      <h3>LOREM IPSUM</h3><p>Lorem Ipsum is simply dummy text of the printing and typesetting industry. Lorem Ipsum has been...</p>
    </div>
    <div class="feature">
      <svg width="34" height="30" viewBox="0 0 34 30"><rect x="8" y="3" width="22" height="16" fill="none" stroke="#2f4a7a" stroke-width="2"/><path d="M4 28V18" stroke="#2f4a7a" stroke-width="3"/></svg>
      <h3>LOREM IPSUM</h3><p>Lorem Ipsum is simply dummy text of the printing and typesetting industry. Lorem Ipsum has been...</p>
    </div>
    <div class="feature">
      <svg width="34" height="30" viewBox="0 0 34 30"><path d="M17 28V8M17 14l-8-6M17 14l8-6M11 28h12" fill="none" stroke="#2f4a7a" stroke-width="2"/></svg>
      <h3>LOREM IPSUM</h3><p>Lorem Ipsum is simply dummy text of the printing and typesetting industry. Lorem Ipsum has been...</p>
    </div>
  </div>
</section>

<div class="abs section-title products-title"><b></b><h2>TON CIEL BRODÉ PRODUCTS</h2><b></b></div>
<div class="abs arrow" style="left:124px"><svg width="30" height="30" viewBox="0 0 30 30"><path d="M17 10l-5 5 5 5" fill="none" stroke="#fff" stroke-width="2"/></svg></div>
<div class="abs arrow" style="left:1044px"><svg width="30" height="30" viewBox="0 0 30 30"><path d="M13 10l5 5-5 5" fill="none" stroke="#fff" stroke-width="2"/></svg></div>
<article class="abs product" style="left:161px"><div class="thumb" role="img" aria-label="Line drawing of a pair of shoes"></div><h3>PRODUCT-1</h3><div class="sku">SKU: 36421537635191</div><div class="price">€85.00</div></article>
<article class="abs product" style="left:384px"><div class="thumb" role="img" aria-label="Line drawing of a lipstick"></div><h3>PRODUCT-2</h3><div class="sku">SKU: 36421537635191</div><div class="price">€20.00</div></article>
<article class="abs product" style="left:607px"><div class="thumb" role="img" aria-label="Line drawing of a shirt"></div><h3>PRODUCT-3</h3><div class="sku">SKU: 36415376135191</div><div class="price">€10.00</div></article>
<article class="abs product" style="left:830px"><div class="thumb" role="img" aria-label="Line drawing of a wristwatch"></div><h3>PRODUCT-4</h3><div class="sku">SKU: 21753712357293</div><div class="price">€25.00</div></article>

<div class="abs blog-bg"></div>
<div class="abs section-title blog-title"><b></b><h2>FROM THE BLOG</h2><b></b></div>
<article class="abs post" style="left:161px"><div class="thumb" role="img" aria-label="Tart on a glass cake stand" style="background:linear-gradient(180deg,#e9ecef,#8a5a34 55%,#cfe0dc)"></div><div class="date">MAY 9, 2017</div><h3>This is your first post</h3><p>Lorem Ipsum is simply dummy text of the printing and typesetting industry. Lorem Ipsum has been the industry's standard dummy text ever since the 1500s, when an unknown printer took a galley of type...</p></article>
<article class="abs post" style="left:459px"><div class="thumb" role="img" aria-label="Green bow tie and flowers on dark wood" style="background:linear-gradient(135deg,#3e3430,#6a8e4c 50%,#3a302b)"></div><div class="date">MAY 9, 2017</div><h3>This is your second post</h3><p>Lorem Ipsum is simply dummy text of the printing and typesetting industry. Lorem Ipsum has been the industry's standard dummy text ever since the 1500s, when an unknown printer took a galley of type...</p></article>
<article class="abs post" style="left:757px"><div class="thumb" role="img" aria-label="Mint sofa with pink cushions in a bright room" style="background:linear-gradient(180deg,#f2f2f0,#9fd1c9 60%,#e6e4e0)"></div><div class="date">MAY 9, 2017</div><h3>This is your second post</h3><p>Lorem Ipsum is simply dummy text of the printing and typesetting industry. Lorem Ipsum has been the industry's standard dummy text ever since the 1500s, when an unknown printer took a galley of type...</p></article>

<section class="abs contact">
  <h2 class="abs">CONTACT WITH US!</h2>
  <div class="abs tag">TON CIEL BRODÉ IS A LEADING ONLINE STORE.</div>
  <div class="abs" style="left:161px;top:120px"><div class="field-label"><svg width="10" height="10" viewBox="0 0 10 10"><circle cx="5" cy="3" r="2.5" fill="#fff"/><path d="M0 10a5 4 0 0 1 10 0z" fill="#fff"/></svg>NAME:</div><div class="field"></div></div>
  <div class="abs" style="left:373px;top:120px"><div class="field-label"><svg width="11" height="9" viewBox="0 0 11 9"><rect width="11" height="9" fill="#fff"/><path d="M0 0l5.5 5L11 0" fill="none" stroke="#4b4741"/></svg>EMAIL</div><div class="field"></div></div>
  <div class="abs" style="left:161px;top:190px"><div class="field-label"><svg width="10" height="10" viewBox="0 0 10 10"><path d="M2 0l2 2-1 2 3 3 2-1 2 2-2 2C4 10 0 6 0 2z" fill="#fff"/></svg>PHONE:</div><div class="field"></div></div>
  <div class="abs" style="left:373px;top:190px"><div class="field-label"><svg width="10" height="10" viewBox="0 0 10 10"><path d="M0 10l1-3 6-6 2 2-6 6z" fill="#fff"/></svg>SUBJECTS</div><div class="field"></div></div>
  <div class="abs" style="left:161px;top:260px"><div class="field-label">COMMENTS:</div><div class="field" style="width:412px;height:108px"></div></div>
  <div class="abs" style="left:161px;top:400px"><span class="btn-dark">READ MORE <i></i></span></div>
</section>
<div class="abs contact-img" role="img" aria-label="Marbling tray with floral pattern and paint jars"></div>

<section class="abs newsletter">
  <h2 class="abs">Newsletter:</h2>
  <div class="abs input">Enter Your Email Id</div>
  <span class="btn-dark">SUBSCRIBE</span>
</section>

<footer class="abs footer">
  <div class="social"><i></i><i></i><i></i><i></i><i></i><i></i></div>
  <p>© 2017 toncielbrode.com. All rights reserved.</p>
</footer>

</body>
</html>
```